Velmora Company

We sell our products into retail stores. We move our Kiosk into the store for a few days, the product sells through, and then we move on to the next store.
Our website is not a place to purchase product. It is only a place that will list the schedule of where/when our kiosk will be in retail stores, and also give the consumer a little more detail about us.
The more you can develop a site that adheres to the theme the better. Want it to be fun and fashionable. Animated ideas are fine, and welcome, but they would need to be coded in HTML5, not flash. So even though this is a design only project, if you are going to recommend some animations, please keep HTML5 in mind.
attached files have:
1. images of the display as seen in the store (without shawls). this is just so you see how we are presenting ourself at retail.
2. images of some of the graphics components that are in the retail display
3. the pdf of the actual words use in the retail display (color meanings). this is the concept that I think as a designer you could really run with. have fun with this one and see how you can thread it into a website.
4. a lot of custom illustrations we had made with the wraps that are in the show. these are part of our theme as well and so you can use these as part of your design. no need to overdo it, use them if it makes sense, or don't use them at all. its fine with us.
Target Market(s)
united states, east coast
Industry/Entity Type
Retail
Requirements
Must have
- 1. Home page that is fashionable, fun, and has a lot of color and play with the color meanings. There should only be 3 links from the home page (about us, contact us, schedules).
2. Secondary page where we will list the schedule for our retail shows. Secondary page should have a simple method for navigating to either the home page or the contact us, about us pages

```html
<!DOCTYPE html>
<html lang="en">
<head>
<meta charset="utf-8">
<title>Velmora Company – Colorful wraps for your wardrobe</title>
<link rel="stylesheet" href="https://fonts.googleapis.com/css2?family=Noto+Serif&family=Quicksand:wght@500&family=Arimo&display=swap">
<style>
  :root {
    --page: #ffffff;
    --paper: #ebe9e8;
    --frame-line: #cfcccb;
    --ribbon: #a39a96;
    --ink: #141414;
    --ink-soft: #2e2a28;
    --mauve: #8e4e6e;
    --green: #3d7148;
    --red: #c03b55;
    --purple: #8e4e6e;
    --orange: #d9785a;
    --indigo: #4a46c8;
    --lavender: #8591c8;
    --blue: #3a7dc4;
    --slate: #7c8a8a;
    --sky: #3dbde9;
    --sketch-light: #e4e2e0;
    --sketch-dark: #cdcac8;
  }
  * { margin: 0; padding: 0; box-sizing: border-box; }
  html, body { width: 1200px; height: 840px; overflow: hidden; background: var(--page); }
  .site {
    position: absolute; left: 24px; top: 0; width: 1152px; height: 822px;
    background: var(--paper); border: 1px solid var(--frame-line); border-top: 0;
  }
  .abs { position: absolute; }
  .top-bar { top: 0; height: 16px; }
  .bottom-bar { top: 762px; height: 30px; }
  .ribbon { left: 22px; top: 0; }
  .brand {
    left: 22px; top: 36px; width: 238px; text-align: center;
    font-family: "Noto Serif", serif; font-size: 52px; color: var(--ink); line-height: 1;
  }
  .tagline {
    left: 22px; top: 132px; width: 238px; text-align: center;
    font-family: "Noto Serif", serif; font-size: 19px; line-height: 23px; color: var(--ink-soft);
  }
  .flourish { left: 106px; width: 86px; height: 14px; border-radius: 7px; background: var(--mauve); opacity: .8; }
  .headline {
    left: 22px; top: 352px; width: 238px; text-align: center;
    font-family: "Noto Serif", serif; font-weight: 400; font-size: 48px; line-height: 55px; color: var(--ink);
  }
  .nav {
    right: 36px; top: 34px; font-family: "Arimo", Arial, sans-serif; font-size: 20px; color: var(--ink);
  }
  .nav a { color: var(--ink); text-decoration: none; }
  .nav .sep { margin: 0 8px; }
  .illustration {
    left: 504px; top: 100px; width: 384px; height: 662px;
    background: linear-gradient(180deg, var(--sketch-light), var(--sketch-dark));
    border-radius: 4px;
  }
  .meaning { border-radius: 50%; }
  .meaning-text {
    font-family: "Quicksand", sans-serif; font-weight: 500; font-size: 22px; line-height: 29px;
    color: #fff; white-space: nowrap; letter-spacing: -0.2px;
  }
  .copyright {
    right: 18px; top: 799px; font-family: "Arimo", Arial, sans-serif; font-size: 12px; color: var(--ink);
  }
</style>
</head>
<body>
<div class="site">
  <div class="abs top-bar" style="left:262px;width:199px;background:var(--green)"></div>
  <div class="abs top-bar" style="left:461px;width:230px;background:var(--red)"></div>
  <div class="abs top-bar" style="left:691px;width:231px;background:var(--purple)"></div>
  <div class="abs top-bar" style="left:922px;width:230px;background:var(--orange)"></div>

  <svg class="abs ribbon" width="238" height="300" viewBox="0 0 238 300" aria-hidden="true">
    <polygon points="0,0 238,0 238,300 119,234 0,300" fill="var(--ribbon)"/>
  </svg>
  <div class="abs brand">Velmora</div>
  <p class="abs tagline">a color or shade<br>the attribute of a<br>color by virtue</p>

  <div class="abs flourish" role="img" aria-label="Mauve swirl ornament" style="top:316px"></div>
  <h1 class="abs headline">Colorful<br>wraps for<br>your<br>wardrobe</h1>
  <div class="abs flourish" role="img" aria-label="Mauve swirl ornament" style="top:596px"></div>

  <svg class="abs" style="left:22px;top:674px" width="238" height="88" viewBox="0 0 238 88" aria-hidden="true">
    <polygon points="0,52 119,0 238,52 238,88 0,88" fill="var(--ribbon)"/>
  </svg>

  <nav class="abs nav">
    <a href="#about">About Us</a><span class="sep">|</span><a href="#schedule">Schedule</a><span class="sep">|</span><a href="#contact">Contact Us</a>
  </nav>

  <div class="abs illustration" role="img" aria-label="Pencil sketch of two women wearing a black scarf and a red scarf"></div>

  <div class="abs meaning" style="left:788px;top:437px;width:130px;height:130px;background:var(--red)"></div>
  <div class="abs meaning" style="left:946px;top:400px;width:150px;height:150px;background:var(--purple)"></div>
  <div class="abs meaning" style="left:903px;top:544px;width:160px;height:160px;background:var(--orange)"></div>
  <div class="abs meaning" style="left:702px;top:557px;width:206px;height:206px;background:var(--green)"></div>

  <p class="abs meaning-text" style="left:808px;top:460px">romance<br>love<br>beauty</p>
  <p class="abs meaning-text" style="left:981px;top:428px">royalty<br>magic<br>mystery</p>
  <p class="abs meaning-text" style="left:928px;top:574px">joy<br>balance<br>endurance</p>
  <p class="abs meaning-text" style="left:732px;top:605px">life<br>nature<br>fortune fertility</p>

  <div class="abs bottom-bar" style="left:0;width:230px;background:var(--indigo)"></div>
  <div class="abs bottom-bar" style="left:230px;width:231px;background:var(--lavender)"></div>
  <div class="abs bottom-bar" style="left:461px;width:230px;background:var(--blue)"></div>
  <div class="abs bottom-bar" style="left:691px;width:231px;background:var(--slate)"></div>
  <div class="abs bottom-bar" style="left:922px;width:230px;background:var(--sky)"></div>

  <p class="abs copyright">Copyright 2011 Velmora. All rights reserved</p>
</div>
</body>
</html>
```